Business card for a young woman who performs life enhancement activities with people who have developmental disabilities, what used to be called retardation. She wants to focus on the creative part of her work. She has a degree in art and will engage clients in art projects as well as helping them learn to do things like grocery shop, cook meals, set goals, and live independently.

Target Market(s)

Parents, caregivers, guardians, relatives of people with developmental disabilities, meaning they have not developed in their mental capacities.

Industry/Entity Type

Business

Contact Information for Business Card

Bright Harbor Services, Marisa T. Dunlop, 417 362-8094, marisa@marisadunlop.example, Life enhancement services for people with developmental disabilities. No address.

Font styles to use
Serif

Requirements
Must have
• Marisa wants it to have some indication of the art or creative part of her work with clients. But it must also be businesslike so it appeals to the parents. They have to see her as a professional, but she's compassionate and artsy. She wants just her company name on the front. The other information should be on the back.

```html
<!DOCTYPE html>
<html lang="en">
<head>
<meta charset="utf-8">
<title>Bright Harbor Services – Business Card</title>
<link rel="stylesheet" href="https://fonts.googleapis.com/css2?family=Source+Serif+4:wght@400&display=swap">
<style>
  :root {
    --ink-blue: #33339a;
    --accent-red: #e8321f;
    --card-white: #ffffff;
    --backdrop: #e9e6e1;
    --photo-light: #e8d3a8;
    --photo-dark: #8a6a5a;
  }
  * { margin: 0; padding: 0; box-sizing: border-box; }
  html, body { width: 1200px; height: 848px; overflow: hidden; }
  body {
    background: var(--backdrop);
    font-family: "Source Serif 4", Georgia, serif;
    position: relative;
  }
  .card {
    position: absolute;
    top: 270px;
    width: 540px;
    height: 309px;
    background: var(--card-white);
    overflow: hidden;
    box-shadow: 0 6px 18px rgba(0,0,0,0.18);
  }
  .card--front { left: 40px; }
  .card--back { left: 620px; }

  .card__swoosh { position: absolute; inset: 0; width: 100%; height: 100%; }

  .portrait {
    position: absolute;
    left: 40px;
    top: 44px;
    width: 200px;
    height: 150px;
    border: 4px solid var(--ink-blue);
    border-radius: 16px;
    background: linear-gradient(135deg, var(--photo-light), var(--photo-dark));
  }

  .contact {
    position: absolute;
    left: 262px;
    top: 26px;
    width: 260px;
    text-align: center;
    color: var(--ink-blue);
  }
  .contact__company { font-size: 24px; line-height: 1.15; }
  .contact__name { font-size: 20px; margin-top: 14px; }
  .contact__phone { font-size: 13px; margin-top: 14px; }
  .contact__email { font-size: 13px; margin-top: 4px; }

  .dot {
    display: inline-block;
    width: 12px;
    height: 12px;
    border-radius: 50%;
    background: var(--accent-red);
    margin-right: 8px;
    vertical-align: middle;
  }
  .brand .dot { width: 16px; height: 16px; margin-right: 12px; }

  .brand {
    position: absolute;
    left: 0;
    right: 0;
    top: 112px;
    text-align: center;
    color: var(--ink-blue);
  }
  .brand__name { font-size: 34px; line-height: 1.2; }
  .brand__tagline { font-size: 14px; margin-top: 16px; }
</style>
</head>
<body>
  <section class="card card--front">
    <svg class="card__swoosh" viewBox="0 0 540 309" preserveAspectRatio="none" aria-hidden="true">
      <path fill="var(--accent-red)" d="M0,226 C150,224 290,208 390,186 C300,214 160,238 0,244 Z"/>
      <path fill="var(--ink-blue)" d="M0,252 C150,246 300,226 400,196 C470,175 510,160 540,150 L540,309 L0,309 Z"/>
    </svg>
    <div class="portrait" role="img" aria-label="Photo of Marisa smiling with a client"></div>
    <div class="contact">
      <p class="contact__company"><span class="dot" aria-hidden="true"></span>Bright Harbor Services</p>
      <p class="contact__name">Marisa T. Dunlop</p>
      <p class="contact__phone">417 362-8094</p>
      <p class="contact__email">marisa@marisadunlop.example</p>
    </div>
  </section>

  <section class="card card--back">
    <div class="brand">
      <p class="brand__name"><span class="dot" aria-hidden="true"></span>Bright Harbor Services</p>
      <p class="brand__tagline">Life enhancement services for people with developmental disabilities</p>
    </div>
  </section>
</body>
</html>
```